Need a flyer to leave behind when visiting clients or at shows

Glossy colorful tri-fold flyer with the same information that is on my web site www.palverdmks.com. I am open to a little modern or creative take on the typical brochure. I created the web site so I can provide any raw files needed from it. I would also like the ability to edit this flyer in the future in Adobe Photoshop Elements

```html
<!DOCTYPE html>
<html lang="en">
<head>
<meta charset="utf-8">
<title>Palverd MKS – Tri-fold Brochure Inside</title>
<link href="https://fonts.googleapis.com/css2?family=Quicksand:wght@500;700&family=Didact+Gothic&display=swap" rel="stylesheet">
<style>
  :root{
    --purple:#6a2c9c;
    --purple-deep:#4f1f7a;
    --purple-soft:#8a56b8;
    --paper:#f4f4f6;
    --paper-shade:#e9e9ee;
    --ink:#1c1c24;
    --white:#ffffff;
    --backdrop:#9a9a9a;
  }
  *{box-sizing:border-box;margin:0;padding:0}
  html,body{width:1200px;height:800px;overflow:hidden}
  body{background:var(--backdrop);font-family:"Didact Gothic",sans-serif;color:var(--ink)}
  .brochure{position:absolute;left:45px;top:60px;width:1110px;height:680px;display:flex;box-shadow:0 14px 30px rgba(0,0,0,.35)}
  .panel{position:relative;width:370px;height:100%;overflow:hidden}
  .panel--objectives{background:var(--paper)}
  .panel--values{background:var(--paper-shade);border-left:1px solid #d6d6dc}
  .panel--services{background:linear-gradient(160deg,#7a37ad 0%,var(--purple) 45%,var(--purple-deep) 100%);color:var(--white)}
  .heading{font-family:"Quicksand",sans-serif;font-weight:700;color:var(--purple);font-size:19px;letter-spacing:.2px}
  .heading .lead{border-bottom:3px solid var(--purple);padding-bottom:1px}
  .panel--services .heading{color:var(--white)}
  .panel--services .heading .lead{border-color:var(--white)}
  .icon-band{position:absolute;background:var(--purple);display:flex;flex-direction:column;justify-content:space-around;align-items:center}
  .icon-band svg{width:34px;height:34px;fill:var(--white)}
  .item-list{position:absolute;list-style:none;font-family:"Quicksand",sans-serif;font-weight:500;font-size:15px;line-height:1.2}
  .photo{position:absolute}
  .objectives-title{position:absolute;left:26px;top:36px}
  .objectives-band{left:26px;top:78px;width:68px;height:196px}
  .objectives-list{left:112px;top:84px;width:240px}
  .objectives-list li{height:66px}
  .photo--clinic{left:0;bottom:0;width:370px;height:330px;background:linear-gradient(150deg,#b9a6cf 0%,#7f5aa6 45%,#553481 100%);clip-path:polygon(0 12%,18% 0,45% 6%,62% 16%,80% 30%,100% 42%,100% 100%,0 100%)}
  .values-title{position:absolute;left:34px;top:36px}
  .values-band{left:34px;top:74px;width:58px;height:232px}
  .values-list{left:112px;top:82px;width:240px}
  .values-list li{height:57px}
  .statement{position:absolute;left:34px;width:310px}
  .statement p{font-size:13.5px;line-height:1.3;margin-top:6px}
  .statement--mission{top:345px}
  .statement--goal{top:440px}
  .statement--goal p{text-align:justify}
  .photo--clinic-edge{left:0;bottom:0;width:250px;height:150px;background:linear-gradient(150deg,#8e6ab5 0%,#5e3a8b 100%);clip-path:polygon(0 35%,30% 20%,55% 0,75% 25%,100% 55%,100% 100%,0 100%)}
  .photo--meeting{left:0;top:0;width:370px;height:200px;background:linear-gradient(180deg,rgba(255,255,255,.12),rgba(255,255,255,0))}
  .services-title{position:absolute;left:30px;top:36px}
  .services-intro{position:absolute;left:30px;top:72px;width:315px;font-size:13px;line-height:1.35}
  .it-title{position:absolute;left:30px;top:210px;font-size:17px}
  .checklist{position:absolute;left:30px;top:250px;list-style:none;font-size:13.5px;line-height:1.75}
  .checklist li::before{content:"✓";margin-right:9px}
  .photo--it{left:0;bottom:0;width:370px;height:250px;background:linear-gradient(135deg,#c9d8ea 0%,#5d84b4 40%,#1f3f6e 100%)}
</style>
</head>
<body>
<div class="brochure">

  <section class="panel panel--objectives">
    <h2 class="heading objectives-title"><span class="lead">Our</span> Primary Objectives</h2>
    <div class="icon-band objectives-band">
      <svg viewBox="0 0 40 40" aria-hidden="true"><circle cx="20" cy="12" r="5"/><circle cx="9" cy="15" r="4"/><circle cx="31" cy="15" r="4"/><path d="M11 32c0-6 4-10 9-10s9 4 9 10z"/><path d="M2 30c0-5 3-8 7-8 2 0 3 .5 4 1.5-2 2-3 4-3 6.5z"/><path d="M38 30c0-5-3-8-7-8-2 0-3 .5-4 1.5 2 2 3 4 3 6.5z"/></svg>
      <svg viewBox="0 0 40 40" aria-hidden="true"><path d="M3 14l8-3 7 4 6-3 13 4v4l-6 8-3 2-3-2-3 2-3-2-3 1-4-4-7-2z"/></svg>
      <svg viewBox="0 0 40 40" aria-hidden="true"><circle cx="20" cy="12" r="6"/><path d="M11 26c0-5 4-8 9-8s9 3 9 8z"/><path d="M20 26v6M9 26l-4 6M31 26l4 6" stroke="#fff" stroke-width="2"/><circle cx="20" cy="34" r="2.5"/><circle cx="5" cy="33" r="2.5"/><circle cx="35" cy="33" r="2.5"/></svg>
    </div>
    <ul class="item-list objectives-list">
      <li>Understand and exceed client expectations</li>
      <li>Committed to be a partner, not vendor</li>
      <li>Provide simplified change management expertise</li>
    </ul>
    <div class="photo photo--clinic" role="img" aria-label="Purple-toned photo of a stethoscope and pen on a medical chart, in a honeycomb arrangement"></div>
  </section>

  <section class="panel panel--values">
    <h2 class="heading values-title"><span class="lead">Our</span> Core Values</h2>
    <div class="icon-band values-band">
      <svg viewBox="0 0 40 40" aria-hidden="true"><circle cx="20" cy="20" r="16" fill="none" stroke="#fff" stroke-width="2"/><circle cx="16" cy="16" r="4"/><circle cx="25" cy="17" r="3.5"/><path d="M9 28c0-4 3-7 7-7s7 3 7 7zM21 27c0-3 2-5 4-5s5 2 5 5z"/></svg>
      <svg viewBox="0 0 40 40" aria-hidden="true"><circle cx="8" cy="10" r="3.5"/><circle cx="32" cy="10" r="3.5"/><rect x="12" y="18" width="16" height="3"/><path d="M5 15h6v9H5zM29 15h6v9h-6zM15 21h2v12h-2zM23 21h2v12h-2zM5 24h2v9H5zM33 24h2v9h-2z"/></svg>
      <svg viewBox="0 0 40 40" aria-hidden="true"><circle cx="15" cy="14" r="8"/><path d="M6 34c0-7 4-11 9-11s9 4 9 11z"/><path d="M22 20h14M29 16v14M24 20l-3 7h6zM34 20l-3 7h6z" stroke="#fff" stroke-width="1.5" fill="none"/></svg>
      <svg viewBox="0 0 40 40" aria-hidden="true"><rect x="5" y="28" width="6" height="8"/><rect x="14" y="23" width="6" height="13"/><rect x="23" y="18" width="6" height="18"/><rect x="32" y="12" width="5" height="24"/><circle cx="17" cy="6" r="3"/><path d="M15 10h4l3 6-2 1-2-3v5h-4v-5l-3 2-1-2z"/></svg>
    </div>
    <ul class="item-list values-list">
      <li>Client Focused</li>
      <li>Accountability</li>
      <li>Integrity</li>
      <li>Professional Development</li>
    </ul>
    <div class="statement statement--mission">
      <h2 class="heading"><span class="lead">Our</span> Mission</h2>
      <p>Partner with clients to increase the value and security of their technology tools.</p>
    </div>
    <div class="statement statement--goal">
      <h2 class="heading"><span class="lead">Our</span> Goal</h2>
      <p>Become the premiere consulting company for Information Technology in the post-acute care industries.</p>
    </div>
    <div class="photo photo--clinic-edge" role="img" aria-label="Continuation of the purple honeycomb photo of a medical chart"></div>
  </section>

  <section class="panel panel--services">
    <div class="photo photo--meeting" role="img" aria-label="Faded photo of a business team meeting under a purple overlay"></div>
    <h2 class="heading services-title"><span class="lead">Our</span> Services</h2>
    <p class="services-intro">We understand different organizations have different needs. Palverd MKS strives to assist your organization by bringing solutions that are easy to understand and allow the client to track success. We provide solutions based on the client's needs and desires.</p>
    <h3 class="heading it-title"><span class="lead">Information</span> Technology</h3>
    <ul class="checklist">
      <li>CIO or IT Director Services</li>
      <li>CISO or Information Security Officer</li>
      <li>Comprehensive ePHI Risk Assessments</li>
      <li>IT Department Evaluation</li>
      <li>Policy Management and Consulting</li>
      <li>On-going IT department support</li>
    </ul>
    <div class="photo photo--it" role="img" aria-label="Photo of a businessman touching a glowing IT hexagon on a digital technology network interface"></div>
  </section>

</div>
</body>
</html>
```